Small Production Wine Needs a Wine Label Design

We need a wine bottle label design for a hand crafted Petite Sirah wine produced by two friends in the wine industry. The wine brand will be called, TK (the first initials of each of their last names, Tavares Kimble). The petite sirah grapes are from the Tavares vineyard in the Russian River Valley of Sonoma County, and Kimble is the winemaker. Tavares is a third generation farmer in sonoma county and also raised cattle on the same ranch the grapes were grown. Kimble is an experienced Winemaker and helped increase the quality of wines from Lodi, CA at a small boutique winery. For the front label, we would like the TK to look like a cattle brand, the font to be color black. We would like to include somewhere on the label Tavares Kimble, maybe underneath the cattle brand in smaller font. We also need to include the appellation on the label, Russian River Valley, and in smaller font Sonoma County. Also, the varietal of the wine is Petite Sirah and the vintage is 2013. We are aiming for a simple and relatively classy label, yet with a rustic touch. We would like the label to be rectangular and have an organic/linen look to it. Also the incorporation of a ridge or mountain range in the back ground or subtly in the label would be cool.

```html
<!DOCTYPE html>
<html lang="en">
<head>
<meta charset="utf-8">
<title>Tavares Kimble – Petite Sirah Label Options</title>
<link rel="stylesheet" href="https://fonts.googleapis.com/css2?family=Cinzel:wght@400;700;900&family=Parisienne&family=Libre+Baskerville&display=swap">
<style>
  :root {
    --page: #ffffff;
    --gold: #d4ae3a;
    --gold-light: #f0dc6a;
    --gold-deep: #b8902a;
    --gold-text: #9a7418;
    --brown-text: #7a5a10;
    --ink: #151515;
    --cream: #f7f0c0;
    --brand-field: #f4ead0;
    --option-red: #ff0000;
  }
  * { box-sizing: border-box; margin: 0; padding: 0; }
  html, body { width: 1200px; height: 1000px; overflow: hidden; background: var(--page); }
  .canvas { position: relative; width: 1200px; height: 1000px; }

  .option-tag {
    position: absolute;
    font-family: Arial, Helvetica, sans-serif;
    font-weight: 400;
    font-variant: small-caps;
    font-size: 70px;
    color: var(--option-red);
    letter-spacing: 1px;
    line-height: 1;
  }
  .option-tag--one { left: 755px; top: 160px; }
  .option-tag--two { left: 145px; top: 780px; }

  .label { position: absolute; }
  .label__frame {
    position: absolute;
    background: linear-gradient(160deg, var(--gold-light), var(--gold) 40%, var(--gold-deep) 100%);
  }
  .label__field { position: absolute; }

  .label__tab {
    position: absolute;
    background: linear-gradient(160deg, var(--gold-light), var(--gold) 50%, var(--gold-deep));
    z-index: 2;
  }
  .label__tab-core {
    position: absolute;
    inset: 14px;
    background: var(--brand-field);
    display: flex; align-items: center; justify-content: center;
  }
  .brand-initials {
    font-family: "Cinzel", serif;
    font-weight: 900;
    font-size: 84px;
    color: var(--ink);
    line-height: 1;
  }

  .label__content { position: absolute; text-align: center; z-index: 3; }
  .brand-name {
    font-family: "Cinzel", serif;
    font-weight: 900;
    font-size: 46px;
    color: var(--ink);
    line-height: 1;
    white-space: nowrap;
  }
  .brand-tagline {
    font-family: "Parisienne", cursive;
    font-size: 36px;
    color: var(--brown-text);
    line-height: 1;
    margin-top: 4px;
    padding-left: 200px;
    white-space: nowrap;
  }
  .varietal {
    display: flex; align-items: center; gap: 4px;
    font-family: "Cinzel", serif;
    font-weight: 700;
    font-size: 29px;
    color: var(--gold-text);
    line-height: 1;
    white-space: nowrap;
  }
  .varietal__rule {
    flex: 1; height: 4px;
    background: linear-gradient(90deg, transparent, var(--gold-deep));
    border-radius: 2px;
  }
  .varietal__rule--right { background: linear-gradient(90deg, var(--gold-deep), transparent); }
  .appellation {
    font-family: "Parisienne", cursive;
    font-size: 44px;
    color: var(--ink);
    line-height: 1;
    white-space: nowrap;
  }
  .county {
    font-family: "Cinzel", serif;
    font-size: 24px;
    color: var(--gold-text);
    line-height: 1;
    margin-top: 2px;
    padding-left: 60px;
    white-space: nowrap;
  }
  .vintage {
    position: absolute;
    font-family: "Libre Baskerville", serif;
    font-size: 24px;
    color: var(--ink);
    z-index: 3;
  }

  /* Option 2 – white label */
  .label--white .label__frame { left: 37px; top: 120px; width: 550px; height: 592px; }
  .label--white .label__field { left: 49px; top: 132px; width: 526px; height: 560px; background: #fff; }
  .label--white .label__tab { left: 215px; top: 40px; width: 192px; height: 192px; }

  /* Option 1 – cream label */
  .label--cream .label__outline {
    position: absolute; left: 611px; top: 367px; width: 565px; height: 603px;
    background: var(--ink); border-radius: 9px;
  }
  .label--cream .label__frame { left: 618px; top: 374px; width: 551px; height: 589px; border-radius: 4px; }
  .label--cream .label__field { left: 634px; top: 390px; width: 519px; height: 557px; background: var(--cream); }
  .label--cream .label__tab-outline {
    position: absolute; left: 790px; top: 285px; width: 200px; height: 200px;
    background: var(--ink); border-radius: 9px; z-index: 2;
  }
  .label--cream .label__tab { left: 796px; top: 291px; width: 188px; height: 188px; }
</style>
</head>
<body>
<main class="canvas">

  <div class="option-tag option-tag--one">Option-1</div>
  <div class="option-tag option-tag--two">Option-2</div>

  <!-- Option 2 -->
  <section class="label label--white" aria-label="Label option two">
    <div class="label__frame"></div>
    <div class="label__field"></div>
    <div class="label__tab"><div class="label__tab-core"><span class="brand-initials">TK</span></div></div>

    <div class="label__content" style="left:60px; top:295px; width:500px;">
      <div class="brand-name">TAVARES KIMBLE</div>
      <div class="brand-tagline">Wine &amp; Ranch</div>
    </div>
    <div class="label__content" style="left:62px; top:432px; width:496px;">
      <div class="varietal"><span class="varietal__rule"></span>Petite Sirah<span class="varietal__rule varietal__rule--right"></span></div>
    </div>
    <div class="label__content" style="left:90px; top:565px; width:450px;">
      <div class="appellation">Russian River Valley</div>
      <div class="county">Sonoma County</div>
    </div>
    <div class="vintage" style="left:488px; top:650px;">2013</div>
  </section>

  <!-- Option 1 -->
  <section class="label label--cream" aria-label="Label option one">
    <div class="label__outline"></div>
    <div class="label__frame"></div>
    <div class="label__field"></div>
    <div class="label__tab-outline"></div>
    <div class="label__tab"><div class="label__tab-core"><span class="brand-initials">TK</span></div></div>

    <div class="label__content" style="left:640px; top:546px; width:510px;">
      <div class="brand-name">TAVARES KIMBLE</div>
      <div class="brand-tagline">Wine &amp; Ranch</div>
    </div>
    <div class="label__content" style="left:643px; top:684px; width:496px;">
      <div class="varietal"><span class="varietal__rule"></span>Petite Sirah<span class="varietal__rule varietal__rule--right"></span></div>
    </div>
    <div class="label__content" style="left:670px; top:815px; width:450px;">
      <div class="appellation">Russian River Valley</div>
      <div class="county">Sonoma County</div>
    </div>
    <div class="vintage" style="left:1068px; top:900px;">2013</div>
  </section>

</main>
</body>
</html>
```